Web Design Project

We are a SaaS company that specializes in the thrift industry POS and inventory software. We want a clean and professional site that does NOT look like a template site.

*** A little more about our business -
We offer a SaaS (Software As A Service) for a Point Of Sale and inventory control product specifically for the Thrift / Second hand industry. The software allows them to process inventory, grade/rate it, create the barcoded tags. It the does the whole retail sale process. We also offer tie-ins to Plumora, Zentiq and pebble/vorn mobile apps to support our customers thrift stores.

We need to in incorporate the look/feel and color scheme of our logo.

I would imagine possibly a HTML5 slideshow (3-5 slides) rotating on the home page showing screenshots, etc.

I am envisioning icons representing features of our product.

PLEASE ask questions, I am sure I have left out a ton.

Reason: I am increasing the budget.

Reason: I have had a harder time with content than I thought I would.

Reason: I was very ill, but I am back and want to get it finished up!

Requirements
Must have
• I have attached a couple of our logo's with color options. It needs to flow with that.

I have also attached a screen shot of what I think might work. This DOESN'T suggest that is what I am looking for, just a sample.

I am thinking a home page and maybe one or two sub pages
***Update, I kind of like the following concept for one of the sub-pages
http://www.quelbrix.example/estimate.html

There should also be a place to highlight Plumora and zentiq.

It will be a bilingual / multilingual site, so take that into account
Should not have
• I don't want it to look like a template site. It should be clean and professional.

```html
<!DOCTYPE html>
<html lang="en">
<head>
<meta charset="utf-8">
<title>Kindly Stock</title>
<link href="https://fonts.googleapis.com/css2?family=Arimo:wght@400;700&family=Roboto:wght@300;400;500&family=Roboto+Condensed:wght@400&display=swap" rel="stylesheet">
<style>
:root{
  --blue:#1596d6;
  --blue-dark:#0b7fc0;
  --ink:#222;
  --grey-text:#555;
  --band:#1b1b1b;
  --footer:#262626;
  --footer-box:#2e2e2e;
  --bottom:#141414;
  --light:#e6e6e6;
  --white:#fff;
}
*{box-sizing:border-box;margin:0;padding:0}
html,body{width:1070px;height:1200px;overflow:hidden}
body{position:relative;background:#efefef;font-family:"Arimo",Arial,sans-serif;color:var(--ink)}
.abs{position:absolute}

/* top bar */
.topbar{left:0;top:0;width:1070px;height:45px;background:var(--blue);color:#111;font-size:13px}
.topbar span{position:absolute;top:15px}
.topbar .sep{top:0;width:1px;height:45px;background:rgba(0,0,0,.15)}

/* header */
.header{left:0;top:45px;width:1070px;height:91px;background:var(--white)}
.brand{left:27px;top:22px;display:flex;align-items:center;gap:10px}
.brand-mark{width:34px;height:34px;background:var(--blue);border-radius:4px}
.brand-name{font-family:"Arimo",sans-serif;font-weight:700;font-size:31px;color:var(--blue)}
.nav{top:36px;font-family:"Roboto",sans-serif;font-size:17px;color:#333}
.nav a{position:absolute;white-space:nowrap;text-decoration:none;color:inherit}
.nav .active{color:var(--blue);border-bottom:2px solid var(--blue);padding:0 4px 6px}

/* dark band */
.band{left:0;top:136px;width:1070px;height:460px;background:var(--band)}
.search{left:11px;top:153px;width:314px;height:36px;background:#bbb;border-radius:3px;padding:3px}
.search-field{width:100%;height:100%;background:var(--white);border-radius:2px;font-size:13px;padding:8px 10px;position:relative}
.search-field svg{position:absolute;right:6px;top:3px}
.sidebar{left:11px;top:200px;width:314px;height:359px;background:var(--white);border-radius:3px;overflow:hidden}
.sidebar-title{height:39px;background:#8c8c8c;color:var(--white);font-family:"Roboto",sans-serif;font-size:17px;padding:10px 14px;position:relative}
.tool{height:36px;background:var(--light);margin-top:6px;position:relative;color:var(--blue);font-weight:700;font-size:14.5px;padding:10px 0 0 52px}
.tool svg.cart{position:absolute;left:18px;top:8px}
.tool svg.chev{position:absolute;right:16px;top:12px}
.sub{list-style:none;padding:8px 0 4px 46px;font-size:12.5px}
.sub li{height:22.5px;position:relative;color:#333}
.sub li::before{content:"";position:absolute;left:-18px;top:4px;width:8px;height:8px;border-radius:50%;background:#555}
.sub li.on{color:#000}.sub li.on::before{background:#111}

.crumbs{left:341px;top:152px;width:718px;height:37px;background:var(--white);border-radius:3px;font-size:12.5px;color:#555;display:flex;align-items:center;gap:12px;padding-left:16px}
.crumbs .dot{width:22px;height:18px;background:var(--blue);border-radius:3px}
.crumbs .arrow{color:var(--blue);font-size:14px}
.hero{left:341px;top:200px;width:718px;height:359px;border:2px solid #3a3a3a;background:linear-gradient(120deg,#b8a78a 0%,#6f6a6a 40%,#7c8492 60%,#c9b8b0 100%)}
.hero-caption{left:0;bottom:0;width:100%;height:70px;background:rgba(0,0,0,.78);color:var(--white);font-size:15px}
.hero-caption .title{position:absolute;left:19px;top:11px}
.hero-caption .links{position:absolute;left:43px;top:37px;display:flex;gap:13px;align-items:center}
.plus{font-size:26px;font-weight:700;line-height:14px;margin:0 6px}

/* content */
.content{left:11px;top:575px;width:1048px;height:352px;background:var(--white);border-radius:4px}
.video{left:27px;top:591px;width:298px;height:253px;border:2px solid #333;background:linear-gradient(135deg,#d9d7d2,#9fa2a6 55%,#c6b4a8)}
.video-bar{left:0;bottom:0;width:100%;height:22px;background:#222;color:#ccc;font-size:9px;padding:5px 0 0 75px}
.card{position:absolute;top:591px;width:214px}
.thumb{width:214px;height:157px;border:1px solid #ccc;padding:5px;background:var(--white);box-shadow:0 1px 3px rgba(0,0,0,.2)}
.thumb div{width:100%;height:100%}
.card h3{font-size:13px;color:var(--blue);margin:16px 0 8px}
.card p{font-size:12.5px;line-height:17px;color:var(--grey-text);text-align:justify}

/* footer */
.footer{left:0;top:927px;width:1070px;height:221px;background:var(--footer)}
.fbox{position:absolute;top:927px;width:321px;height:199px;background:var(--footer-box);border:1px solid #1a1a1a;border-top:none;color:#bbb;font-size:12.5px;line-height:19px;padding:0 15px}
.fbox h2{font-family:"Roboto Condensed",sans-serif;font-weight:400;font-size:20px;color:#ddd;margin-top:16px;padding-bottom:8px;border-bottom:1px solid #555;width:175px}
.fbox .icon{position:absolute;right:14px;top:10px}
.fbox .date,.fbox .more{color:#5cc8ff}
.subscribe{margin:18px 0 14px;height:38px;background:#555;border-radius:3px;padding:3px;display:flex}
.subscribe .field{flex:1;background:#ddd;border-radius:2px 0 0 2px}
.subscribe .btn{width:100px;background:var(--blue);color:var(--white);font-weight:700;font-size:16px;text-align:center;padding-top:6px}
.bottom{left:0;top:1148px;width:1070px;height:52px;background:var(--bottom);color:#bbb;font-size:12.5px;text-align:center;padding-top:17px}
</style>
</head>
<body>

<div class="abs topbar">
  <span style="left:27px">English &#8964;</span>
  <div class="abs sep" style="left:103px"></div>
  <span style="left:121px">Cutomer Service</span>
  <div class="abs sep" style="left:232px"></div>
  <span style="left:248px">Call Us : 555.010.0147</span>
  <span style="left:953px">Register / Login</span>
</div>

<header class="abs header">
  <div class="abs brand"><div class="brand-mark"></div><div class="brand-name">kindlystock</div></div>
  <nav class="abs nav" style="left:0;width:1070px">
    <a class="active" style="left:459px">Home</a>
    <a style="left:546px">About Us</a>
    <a style="left:651px">Customers</a>
    <a style="left:767px">Pricing</a>
    <a style="left:857px">Solutions</a>
    <a style="left:964px">Contact Us</a>
  </nav>
</header>

<div class="abs band"></div>

<div class="abs search"><div class="search-field">Search
  <svg width="24" height="24" viewBox="0 0 24 24"><circle cx="10" cy="10" r="7" fill="none" stroke="#1596d6" stroke-width="2.5"/><line x1="15" y1="15" x2="22" y2="22" stroke="#1596d6" stroke-width="3"/></svg>
</div></div>

<aside class="abs sidebar">
  <div class="sidebar-title">Quick Tools
    <svg style="position:absolute;right:14px;top:16px" width="14" height="8"><polygon points="0,0 14,0 7,8" fill="#fff"/></svg>
  </div>
  <div class="tool">POS Store Front<svg class="cart" width="24" height="20" viewBox="0 0 24 20"><path d="M1 2h4l3 11h12l3-8H7" fill="none" stroke="#1596d6" stroke-width="2"/><circle cx="10" cy="17" r="2" fill="#1596d6"/><circle cx="18" cy="17" r="2" fill="#1596d6"/></svg><svg class="chev" width="8" height="13"><polygon points="0,0 8,6.5 0,13" fill="#666"/></svg></div>
  <div class="tool">POS Store Front<svg class="cart" width="24" height="20" viewBox="0 0 24 20"><path d="M1 2h4l3 11h12l3-8H7" fill="none" stroke="#1596d6" stroke-width="2"/><circle cx="10" cy="17" r="2" fill="#1596d6"/><circle cx="18" cy="17" r="2" fill="#1596d6"/></svg><svg class="chev" style="top:14px" width="13" height="8"><polygon points="0,0 13,0 6.5,8" fill="#1596d6"/></svg></div>
  <ul class="sub">
    <li class="on">Lorem Ipsum is simply dummy</li>
    <li>Lorem Ipsum is simply dummy</li>
    <li>Lorem Ipsum is simply dummy</li>
    <li>Lorem Ipsum is simply dummy</li>
  </ul>
  <div class="tool">POS Store Front<svg class="cart" width="24" height="20" viewBox="0 0 24 20"><path d="M1 2h4l3 11h12l3-8H7" fill="none" stroke="#1596d6" stroke-width="2"/><circle cx="10" cy="17" r="2" fill="#1596d6"/><circle cx="18" cy="17" r="2" fill="#1596d6"/></svg><svg class="chev" width="8" height="13"><polygon points="0,0 8,6.5 0,13" fill="#666"/></svg></div>
  <div class="tool">POS Store Front<svg class="cart" width="24" height="20" viewBox="0 0 24 20"><path d="M1 2h4l3 11h12l3-8H7" fill="none" stroke="#1596d6" stroke-width="2"/><circle cx="10" cy="17" r="2" fill="#1596d6"/><circle cx="18" cy="17" r="2" fill="#1596d6"/></svg><svg class="chev" width="8" height="13"><polygon points="0,0 8,6.5 0,13" fill="#666"/></svg></div>
  <div class="tool">POS Store Front<svg class="cart" width="24" height="20" viewBox="0 0 24 20"><path d="M1 2h4l3 11h12l3-8H7" fill="none" stroke="#1596d6" stroke-width="2"/><circle cx="10" cy="17" r="2" fill="#1596d6"/><circle cx="18" cy="17" r="2" fill="#1596d6"/></svg><svg class="chev" width="8" height="13"><polygon points="0,0 8,6.5 0,13" fill="#666"/></svg></div>
</aside>

<div class="abs crumbs"><div class="dot"></div><span class="arrow">&#10095;</span>Quick Tools<span class="arrow">&#10095;</span>POS Store Front<span class="arrow">&#10095;</span>Lorem Ipsum is simply dummy</div>

<div class="abs hero" role="img" aria-label="Photo of a card payment terminal on a shop counter">
  <div class="abs hero-caption">
    <div class="title">Our POS Systems</div>
    <div class="links">Hardware<span class="plus">+</span>Software<span class="plus">+</span>Payment Processing<span class="plus">+</span>Services</div>
  </div>
</div>

<main class="abs content"></main>
<div class="abs video" role="img" aria-label="Video still of a hand entering a PIN on a card terminal">
  <div class="abs video-bar">00:00 / 10:00</div>
</div>
<div class="card" style="left:341px">
  <div class="thumb"><div role="img" aria-label="Photo of a contactless card tap" style="background:linear-gradient(135deg,#e8e8e8,#8c8c8c 55%,#dcdcdc)"></div></div>
  <h3>Lorem Ipsum is simply dummy</h3>
  <p>Lorem Ipsum is simply dummy text of the printing and typesetting industry. Lorem Ipsum has been the industry's standard dummy text ever since the 1500s, when an unknown printer took a galley of type and scrambled it to make a type specimen book.</p>
</div>
<div class="card" style="left:585px">
  <div class="thumb"><div role="img" aria-label="Photo of a shopper paying with a phone" style="background:linear-gradient(135deg,#d9aeb4,#2a8fa6 50%,#c86b8a)"></div></div>
  <h3>Lorem Ipsum is simply dummy</h3>
  <p>Lorem Ipsum is simply dummy text of the printing and typesetting industry. Lorem Ipsum has been the industry's standard dummy text ever since the 1500s, when an unknown printer took a galley of type and scrambled it to make a type specimen book.</p>
</div>
<div class="card" style="left:829px">
  <div class="thumb"><div role="img" aria-label="Photo of a card terminal in a small shopping cart" style="background:linear-gradient(135deg,#f2f2f2,#9a9a9a 55%,#eeeeee)"></div></div>
  <h3>Lorem Ipsum is simply dummy</h3>
  <p>Lorem Ipsum is simply dummy text of the printing and typesetting industry. Lorem Ipsum has been the industry's standard dummy text ever since the 1500s, when an unknown printer took a galley of type and scrambled it to make a type specimen book.</p>
</div>

<footer class="abs footer"></footer>
<section class="fbox" style="left:32px">
  <h2>Recent Blog Posts</h2>
  <svg class="icon" width="36" height="36" viewBox="0 0 36 36"><path d="M6 30l3-9L25 5l6 6-16 16z" fill="#777"/></svg>
  <div class="date" style="margin-top:14px">9/1/2012</div>
  <div>Lorem Ipsum is simply dummy text of the printing and typesetting industry.</div>
</section>
<section class="fbox" style="left:375px">
  <h2>Recent Zentiq</h2>
  <svg class="icon" width="36" height="36"><circle cx="18" cy="18" r="15" fill="#777"/></svg>
  <div style="margin-top:12px"><span class="date">about 8 hours ago</span> Lorem Ipsum is simply dummy text of the printing and typesetting industry. Lorem Ipsum has been the industry's standard dummy text ever since the 1500s, when an unknown printer took a galley of type and scrambled.</div>
  <div class="more" style="font-weight:700;margin-top:4px">There are many</div>
</section>
<section class="fbox" style="left:717px">
  <h2>Subscribe to Updates</h2>
  <svg class="icon" width="44" height="36" viewBox="0 0 44 36"><path d="M2 14L22 2l20 12v20H2z" fill="#777"/><path d="M2 14l20 12 20-12" fill="none" stroke="#2e2e2e" stroke-width="2"/></svg>
  <div class="subscribe"><div class="field"></div><div class="btn">Subscribe</div></div>
  <div>Lorem Ipsum is simply dummy text of the printing and typesetting industry. Lorem Ipsum has been the industry's standard dummy text ever since the 1500s,</div>
</section>
<div class="abs bottom">Copyright @ 2012, Kindly Stock. All Rights Reserved</div>

</body>
</html>
```